International Psychology Practitioner, Educator and Researcher

I need a new website (or upgrade from existing square space. I provide innovative, client focused, services that are evidence based, specializing in crisis intervention, addiction and other mental health. I am also a researcher and university professor committed to excellence in education. I’m building on an existing practice (www.tidewellpath.ca) and incorporating my personal/professional grade. I would like to see designs that use neutral colours and that incorporate crisp clear lines in a professional and inviting way. The final design should communicate professionalism and approachability. (New head shots and stills to follow)

Target Market(s)

Seeking therapy

Industry/Entity Type

Psychology

Coding

Coded - Design and coding required

Number of Pages Required

3 page

Font styles to use
Sans Serif

Requirements
Must have
• A friendly, warm, crisp feel - professional
Nice to have
• Each tones

```html
<!DOCTYPE html>
<html lang="en">
<head>
<meta charset="utf-8">
<title>TidewellPath.ca — Psychology, Research &amp; Teaching</title>
<link rel="stylesheet" href="https://fonts.googleapis.com/css2?family=Nunito+Sans:wght@300;400;600;700&display=swap">
<style>
:root{
  --paper:#faf7f3;
  --sand:#ede5da;
  --taupe:#8c7a6b;
  --taupe-dark:#75655a;
  --accent:#a8876c;
  --white:#ffffff;
  --ink:#3a332e;
  --body:#5f5750;
  --line:#e2d8cc;
  --hero-top:#efe9dc;
  --hero-mid:#d3ccb8;
  --hero-low:#9a9a82;
}
*{margin:0;padding:0;box-sizing:border-box}
html,body{width:1200px;height:3664px;overflow:hidden}
body{position:relative;background:var(--paper);font-family:'Nunito Sans',Arial,sans-serif;color:var(--body)}
.abs{position:absolute}
.btn{position:absolute;display:flex;align-items:center;justify-content:center;border-radius:30px;background:var(--accent);color:var(--white);font-size:14px;font-weight:700;letter-spacing:.6px;text-transform:uppercase;text-decoration:none}
.btn--light{background:var(--white);color:var(--taupe-dark)}

/* header */
.hero{left:0;top:0;width:1200px;height:626px;background:linear-gradient(180deg,var(--hero-top) 0%,#e4ddcb 40%,var(--hero-mid) 65%,var(--hero-low) 100%)}
.hero-rule{left:0;top:626px;width:1200px;height:2px;background:var(--line)}
.brand{left:111px;top:22px;font-size:26px;font-weight:600;color:var(--ink)}
.nav{left:402px;top:30px;display:flex;gap:24px;font-size:15px;font-weight:600}
.nav a{color:var(--ink);text-decoration:none}
.nav a.is-active{color:var(--accent)}
.social{display:flex;gap:8px}
.social span{width:34px;height:34px;border-radius:50%;border:2px solid var(--accent);display:block}
.social span:first-child{background:var(--accent)}
.social--top{left:970px;top:24px}
.hero-title{left:111px;top:264px;font-size:40px;font-weight:300;color:var(--ink);letter-spacing:-.3px}
.hero-btn{left:299px;top:348px;width:168px;height:50px}

/* section titles */
.section-title{left:0;width:1200px;text-align:center;font-size:44px;font-weight:300;color:var(--ink);letter-spacing:.5px}
.section-title::after{content:"";display:block;width:140px;height:2px;margin:14px auto 0;background:var(--accent)}
.section-title--light{color:var(--white)}
.section-title--light::after{background:var(--white)}

/* about */
.about-title{top:724px}
.about-copy{left:175px;top:830px;width:850px;text-align:center;font-size:15.5px;line-height:26px}
.about-copy p+p{margin-top:18px}
.about-btn{left:525px;top:1014px;width:150px;height:51px}

/* bands */
.band{left:0;width:1200px;background:var(--taupe);border-top:6px solid var(--sand);border-bottom:6px solid var(--sand)}

/* services */
.services-title{top:1258px}
.service-card{position:absolute;width:313px;height:346px;background:var(--white);border-radius:8px;box-shadow:0 4px 12px rgba(60,45,35,.16);text-align:center;padding:26px 14px 0}
.service-icon{width:62px;height:62px;margin:0 auto;border-radius:50%;border:2px solid var(--accent);display:flex;align-items:center;justify-content:center}
.service-icon svg{width:28px;height:28px}
.service-name{margin-top:16px;font-size:20px;font-weight:600;color:var(--ink);line-height:27px}
.service-text{margin-top:16px;font-size:13.5px;line-height:23px;color:var(--body)}
.read-more{position:absolute;left:0;right:0;bottom:24px;display:flex;justify-content:center;align-items:center;gap:8px;color:var(--accent);font-size:14px;font-weight:700;letter-spacing:.4px;text-transform:uppercase}
.read-more svg{width:14px;height:14px}
.consult-btn{left:512px;top:2133px;width:176px;height:49px}

/* corporate */
.corporate-title{top:2372px}
.client-card{position:absolute;top:2491px;width:302px;height:270px;background:var(--white);border-radius:6px;box-shadow:0 3px 10px rgba(60,45,35,.12);padding:8px 8px 0}
.client-image{width:286px;height:199px}
.client-label{margin-top:20px;text-align:center;color:var(--accent);font-size:18px;font-weight:600;text-transform:uppercase;letter-spacing:.6px}

/* testimonial */
.portrait-frame{left:111px;top:2940px;width:294px;height:307px;background:var(--white);padding:8px}
.portrait{width:278px;height:291px;background:linear-gradient(160deg,#d9c3a8,#b89a7c)}
.quote{left:500px;top:3018px;width:620px;color:var(--white);font-size:34px;font-weight:300;line-height:50px}
.quote-name{left:500px;top:3130px;color:var(--white);font-size:44px;font-weight:600}

/* footer */
.foot-head{top:3392px;color:var(--accent);font-size:19px;font-weight:700}
.foot-list{top:3440px;list-style:none;font-size:15px;color:var(--body)}
.foot-list li{display:flex;gap:20px;align-items:flex-start;line-height:26px;margin-bottom:2px}
.foot-list svg{flex:none;width:14px;height:14px;margin-top:6px}
.foot-brand{left:870px;top:3400px;font-size:24px;font-weight:600;color:var(--ink)}
.foot-btn{left:893px;top:3482px;width:168px;height:50px}
.foot-rule{left:111px;top:3601px;width:978px;height:1px;background:var(--line)}
.copyright{left:0;width:1200px;top:3619px;text-align:center;font-size:13px;color:var(--ink)}
.social--foot{left:970px;top:3612px}
</style>
</head>
<body>

<!-- header & hero -->
<div class="abs hero" role="img" aria-label="Photo of a person with raised arms standing on a mountain top above a valley at sunrise"></div>
<div class="abs hero-rule"></div>

<div class="abs brand">TidewellPath.ca</div>
<nav class="abs nav">
  <a class="is-active" href="#">Home</a>
  <a href="#">About Us</a>
  <a href="#">Our Services</a>
  <a href="#">Corporate Clients</a>
  <a href="#">Contact Us</a>
</nav>
<div class="abs social social--top" aria-label="Social links"><span></span><span></span><span></span></div>

<h1 class="abs hero-title">Get ready to take control of your life.</h1>
<a class="btn hero-btn" href="#">Schedule Now</a>

<!-- about -->
<h2 class="abs section-title about-title">About Us</h2>
<div class="abs about-copy">
  <p>We are a specialized practice providing qualified, evidence based and compassionate care online and in person, with a focus on crisis intervention, addiction and mental health. We use a safe, holistic and trauma informed method designed to help you make the changes you want to make.</p>
  <p>Our work is shaped by active research and university teaching, so every session draws on current evidence and a lasting commitment to excellence in education and care.</p>
</div>
<a class="btn about-btn" href="#">Learn More</a>

<!-- services -->
<div class="abs band" style="top:1190px;height:1062px"></div>
<h2 class="abs section-title section-title--light services-title">Our Services</h2>

<article class="service-card" style="left:111px;top:1368px">
  <div class="service-icon"><svg viewBox="0 0 28 28"><path d="M14 24s-9-5.5-9-12a5 5 0 0 1 9-3 5 5 0 0 1 9 3c0 6.5-9 12-9 12z" fill="none" stroke="#a8876c" stroke-width="2"/></svg></div>
  <h3 class="service-name">Crisis<br>Intervention</h3>
  <p class="service-text">Immediate, calm and skilled support when life feels overwhelming. We help you find safety, steady your situation and build a clear plan for the days ahead, online or in person.</p>
  <div class="read-more">Read More <svg viewBox="0 0 14 14"><circle cx="7" cy="7" r="7" fill="#a8876c"/><path d="M5 4l3.5 3L5 10" stroke="#fff" stroke-width="1.8" fill="none"/></svg></div>
</article>
<article class="service-card" style="left:444px;top:1368px">
  <div class="service-icon"><svg viewBox="0 0 28 28"><path d="M4 20l6-6 4 4 10-10" fill="none" stroke="#a8876c" stroke-width="2"/><path d="M18 8h6v6" fill="none" stroke="#a8876c" stroke-width="2"/></svg></div>
  <h3 class="service-name">Addiction &amp;<br>Recovery</h3>
  <p class="service-text">For many people the first step towards change with addiction is acknowledging their personal struggle. The next step is finding resources and support that can help restore their overall wellbeing.</p>
  <div class="read-more">Read More <svg viewBox="0 0 14 14"><circle cx="7" cy="7" r="7" fill="#a8876c"/><path d="M5 4l3.5 3L5 10" stroke="#fff" stroke-width="1.8" fill="none"/></svg></div>
</article>
<article class="service-card" style="left:776px;top:1368px">
  <div class="service-icon"><svg viewBox="0 0 28 28"><circle cx="14" cy="10" r="5" fill="none" stroke="#a8876c" stroke-width="2"/><path d="M5 24c1-5 5-7 9-7s8 2 9 7" fill="none" stroke="#a8876c" stroke-width="2"/></svg></div>
  <h3 class="service-name">Mental Health<br>Counselling</h3>
  <p class="service-text">Evidence based therapy for anxiety, depression, trauma and stress. Sessions are client focused and trauma informed, shaped around your goals, your pace and your values.</p>
  <div class="read-more">Read More <svg viewBox="0 0 14 14"><circle cx="7" cy="7" r="7" fill="#a8876c"/><path d="M5 4l3.5 3L5 10" stroke="#fff" stroke-width="1.8" fill="none"/></svg></div>
</article>
<article class="service-card" style="left:111px;top:1733px">
  <div class="service-icon"><svg viewBox="0 0 28 28"><rect x="6" y="4" width="16" height="20" rx="2" fill="none" stroke="#a8876c" stroke-width="2"/><path d="M10 11l2 2 4-4M10 18h8" fill="none" stroke="#a8876c" stroke-width="2"/></svg></div>
  <h3 class="service-name">Psychological<br>Assessment</h3>
  <p class="service-text">We believe in science! We use a range of validated psychometric testing to help you understand who you are, how you see things and how you interact with the world.</p>
  <div class="read-more">Read More <svg viewBox="0 0 14 14"><circle cx="7" cy="7" r="7" fill="#a8876c"/><path d="M5 4l3.5 3L5 10" stroke="#fff" stroke-width="1.8" fill="none"/></svg></div>
</article>
<article class="service-card" style="left:444px;top:1733px">
  <div class="service-icon"><svg viewBox="0 0 28 28"><circle cx="12" cy="12" r="7" fill="none" stroke="#a8876c" stroke-width="2"/><path d="M17 17l7 7" stroke="#a8876c" stroke-width="2"/></svg></div>
  <h3 class="service-name">Research &amp;<br>Evidence</h3>
  <p class="service-text">Our practice is grounded in active research. Findings from ongoing studies in crisis care, addiction and recovery shape the methods we bring to every session we offer.</p>
  <div class="read-more">Read More <svg viewBox="0 0 14 14"><circle cx="7" cy="7" r="7" fill="#a8876c"/><path d="M5 4l3.5 3L5 10" stroke="#fff" stroke-width="1.8" fill="none"/></svg></div>
</article>
<article class="service-card" style="left:776px;top:1733px">
  <div class="service-icon"><svg viewBox="0 0 28 28"><path d="M3 11l11-5 11 5-11 5z" fill="none" stroke="#a8876c" stroke-width="2"/><path d="M8 14v5c3 3 9 3 12 0v-5" fill="none" stroke="#a8876c" stroke-width="2"/></svg></div>
  <h3 class="service-name">Teaching &amp;<br>Training</h3>
  <p class="service-text">University teaching and professional workshops for students, clinicians and teams who want practical, evidence based skills in mental health and crisis care.</p>
  <div class="read-more">Read More <svg viewBox="0 0 14 14"><circle cx="7" cy="7" r="7" fill="#a8876c"/><path d="M5 4l3.5 3L5 10" stroke="#fff" stroke-width="1.8" fill="none"/></svg></div>
</article>

<a class="btn btn--light consult-btn" href="#">Book a Consult</a>

<!-- corporate clients -->
<h2 class="abs section-title corporate-title">Corporate Clients</h2>
<div class="client-card" style="left:122px">
  <div class="client-image" role="img" aria-label="Photo of a bright office lounge with chairs and a lamp" style="background:linear-gradient(180deg,#e9dfd1,#cfc8bc)"></div>
  <div class="client-label">Employee Selection</div>
</div>
<div class="client-card" style="left:449px">
  <div class="client-image" role="img" aria-label="Photo of grey paper head cut-outs with one colourful head" style="background:linear-gradient(135deg,#bdb8b2,#918b85)"></div>
  <div class="client-label">Testing &amp; Reporting</div>
</div>
<div class="client-card" style="left:776px">
  <div class="client-image" role="img" aria-label="Photo of a sticky note about conflict on a desk" style="background:linear-gradient(135deg,#f0ede8,#d6dfe2)"></div>
  <div class="client-label">Conflict Resolution</div>
</div>

<!-- testimonial -->
<div class="abs band" style="top:2880px;height:440px"></div>
<div class="abs portrait-frame"><div class="portrait" role="img" aria-label="Portrait photo of a smiling client"></div></div>
<blockquote class="abs quote">“I dreamed big! I’m now in my dream career living my best life”</blockquote>
<div class="abs quote-name">- Maya R.</div>

<!-- footer -->
<h4 class="abs foot-head" style="left:111px">Menu</h4>
<ul class="abs foot-list" style="left:111px">
  <li><svg viewBox="0 0 14 14"><circle cx="7" cy="7" r="7" fill="#a8876c"/><path d="M5 4l3.5 3L5 10" stroke="#fff" stroke-width="1.8" fill="none"/></svg>Home</li>
  <li><svg viewBox="0 0 14 14"><circle cx="7" cy="7" r="7" fill="#a8876c"/><path d="M5 4l3.5 3L5 10" stroke="#fff" stroke-width="1.8" fill="none"/></svg>About Us</li>
  <li><svg viewBox="0 0 14 14"><circle cx="7" cy="7" r="7" fill="#a8876c"/><path d="M5 4l3.5 3L5 10" stroke="#fff" stroke-width="1.8" fill="none"/></svg>Our Services</li>
  <li><svg viewBox="0 0 14 14"><circle cx="7" cy="7" r="7" fill="#a8876c"/><path d="M5 4l3.5 3L5 10" stroke="#fff" stroke-width="1.8" fill="none"/></svg>Corporate Clients</li>
  <li><svg viewBox="0 0 14 14"><circle cx="7" cy="7" r="7" fill="#a8876c"/><path d="M5 4l3.5 3L5 10" stroke="#fff" stroke-width="1.8" fill="none"/></svg>Contact Us</li>
</ul>

<h4 class="abs foot-head" style="left:344px">Contact Us</h4>
<ul class="abs foot-list" style="left:344px">
  <li><svg viewBox="0 0 14 14"><path d="M7 1a4.5 4.5 0 0 0-4.5 4.5C2.5 9 7 13 7 13s4.5-4 4.5-7.5A4.5 4.5 0 0 0 7 1z" fill="#a8876c"/><circle cx="7" cy="5.5" r="1.6" fill="#faf7f3"/></svg>3-118 Harbourline Road<br>Millbay, BC, Canada</li>
  <li style="margin-top:10px"><svg viewBox="0 0 14 14"><rect x="1" y="3" width="12" height="8" rx="1" fill="#a8876c"/><path d="M1.5 3.5L7 8l5.5-4.5" stroke="#faf7f3" stroke-width="1.2" fill="none"/></svg>hello@tidewellpath.ca</li>
  <li style="margin-top:8px"><svg viewBox="0 0 14 14"><path d="M3 1.5l2.2 2.6-1.3 1.6c.8 1.7 2.2 3.1 3.9 3.9l1.6-1.3 2.6 2.2-1.2 1.8C6 12 2 8 1.5 3z" fill="#a8876c"/></svg>(250) 555-0184</li>
</ul>

<h4 class="abs foot-head" style="left:643px">Hours</h4>
<ul class="abs foot-list" style="left:643px">
  <li><svg viewBox="0 0 14 14"><circle cx="7" cy="7" r="6" stroke="#a8876c" stroke-width="1.6" fill="none"/><path d="M7 3.5V7l2.2 1.5" stroke="#a8876c" stroke-width="1.4" fill="none"/></svg>Monday — Friday<br>9am — 5pm</li>
  <li style="margin-top:10px"><svg viewBox="0 0 14 14"><circle cx="7" cy="7" r="6" stroke="#a8876c" stroke-width="1.6" fill="none"/><path d="M7 3.5V7l2.2 1.5" stroke="#a8876c" stroke-width="1.4" fill="none"/></svg>Saturday<br>9am — 1pm</li>
</ul>

<div class="abs foot-brand">TidewellPath.ca</div>
<a class="btn foot-btn" href="#">Schedule Now</a>

<div class="abs foot-rule"></div>
<p class="abs copyright">© 2021 TidewellPath.ca. All Rights Reserved</p>
<div class="abs social social--foot" aria-label="Social links"><span></span><span></span><span></span></div>

</body>
</html>
```